Real Estate Brokerage - Sales Promo Flyer

We would like someone to design a 8x11 high gloss promotional flyer for our real estate agents to use in the field when presenting to a possible listing client (someone who wants to sell their home).

The flyer should include some of our brokerage's recent sales transaction numbers, as well as benefits to using our service.

We would like our design to have a professional appeal, with bold colors, and vivid images.

I have attached 5 images of recently sold homes:
247 Marisol Lane Trust, Palm Beach Gardens, Florida - Sold for $424,000
4718 Tierra Linda Ct, Boca Raton, FL 33431 - Sold for $415,000
418 Verbena Hills Drive, Palm Beach Gardens, Florida - Sold for $877,500
20417 Heron Bluff Circle, West Palm Beach, Florida - Sold for $380,000
382 Thistle Road, Greenacres, Florida - Sold for $234,500

I can provide any additional details you need. See attached files.
Updates

This flyer should contain our business name, logo, phone numbers, and website (however you see fit). PelicoHomes Palm Beach County | (561) 402-1186 Broward County | (954) 238-4417 www.pelicohomes-example.com

More Properties to Add: 418 Verbena Hills Drive, Palm Beach Gardens, Florida - Sold for $877,500 20417 Heron Bluff Circle, West Palm Beach, Florida - Sold for $380,000 382 Thistle Road, Greenacres, Florida - Sold for $234,500

I have added the Original Logo Images. Please use one of these in your design.

I have uploaded an image of our syndication partners, please add this to your flyers.

Please submit all of your Design. Thanks!

Please submit your edits

Industry/Entity Type

Real Estate

Requirements
Must have
• PelicoHomes is one word with a capital K and capital R.

Must have website and phone number.

PelicoHomes
www.pelicohomes-example.com
561-402-1186 - Palm Beach County
954-238-4417 - Broward County

```html
<!DOCTYPE html>
<html lang="en">
<head>
<meta charset="utf-8">
<title>PelicoHomes – Elegant Homes for Sale</title>
<link rel="stylesheet" href="https://fonts.googleapis.com/css2?family=Signika:wght@400;600;700&family=Quicksand:wght@500;600&family=Lora:wght@400;600&display=swap">
<style>
  :root {
    --page-bg: #e3e3e3;
    --ink-dark: #1f2325;
    --teal-deep: #1e5a5c;
    --teal-mid: #2a8487;
    --teal-bright: #2db5bd;
    --teal-pale: #b5e2e2;
    --paper: #f3f7f7;
    --badge-red: #e4432b;
    --badge-gold: #ffd873;
    --tick-red: #e33a2a;
    --white: #ffffff;
    --text-grey: #4a5050;
  }
  * { box-sizing: border-box; margin: 0; padding: 0; }
  html, body { width: 1200px; height: 795px; overflow: hidden; }
  body { background: var(--page-bg); position: relative; font-family: "Signika", sans-serif; }

  .flyer {
    position: absolute; left: 465px; top: 67px; width: 480px; height: 633px;
    background: var(--white); overflow: hidden;
    box-shadow: 0 6px 18px rgba(0,0,0,.18);
  }
  .hero-photo {
    position: absolute; left: 0; top: 0; width: 480px; height: 275px;
    background: linear-gradient(180deg, #8fc4ea 0%, #cfe3ef 22%, #d8cfb4 40%, #c9bb97 62%, #6f8f5a 82%, #8e7a66 100%);
  }
  .brand-tab {
    position: absolute; left: 10px; top: 0; width: 165px; height: 83px;
    background: var(--ink-dark); border-radius: 0 0 10px 0;
    display: flex; align-items: flex-end; justify-content: center; gap: 8px; padding-bottom: 14px;
  }
  .brand-mark { width: 12px; height: 12px; border-radius: 50%; background: var(--teal-bright); margin-bottom: 4px; }
  .brand-name { font-family: "Signika", sans-serif; font-weight: 600; color: var(--white); font-size: 18px; letter-spacing: 1.5px; }

  .sold-badge { position: absolute; left: 40px; top: 170px; width: 116px; height: 116px; }

  .feature-panel {
    position: absolute; left: 0; top: 245px; width: 480px; height: 170px;
    background: var(--teal-deep);
    clip-path: polygon(0 22%, 100% 0, 100% 100%, 0 100%);
  }
  .feature-panel::after {
    content: ""; position: absolute; left: 170px; top: 0; width: 310px; height: 170px;
    background: linear-gradient(100deg, var(--teal-mid), #2f9a9c);
    clip-path: polygon(18% 0, 100% 0, 100% 100%, 0 100%);
  }

  .recent-sale { position: absolute; top: 228px; width: 110px; text-align: center; }
  .recent-sale .thumb {
    width: 82px; height: 82px; margin: 0 auto; border-radius: 50%; border: 4px solid var(--white);
    background: linear-gradient(180deg, #9fcbe8 0%, #dfe6e6 40%, #c8c3b0 58%, #6e9a52 80%, #5f8a48 100%);
  }
  .recent-sale .addr { font-family: "Lora", serif; font-size: 7.5px; line-height: 1.3; color: var(--white); margin-top: 6px; }
  .recent-sale .price { font-family: "Lora", serif; font-weight: 600; font-size: 8.5px; color: var(--white); margin-top: 3px; }
  .sale-1 { left: 175px; }
  .sale-2 { left: 260px; }
  .sale-3 { left: 350px; }

  .headline {
    position: absolute; left: 30px; top: 298px; color: var(--white);
    font-family: "Signika", sans-serif; font-weight: 600; font-size: 29px; line-height: 1.02; letter-spacing: .3px;
  }
  .spec-list { position: absolute; top: 355px; list-style: none; font-family: "Quicksand", sans-serif; font-weight: 600; font-size: 14.5px; color: var(--white); }
  .spec-list li { display: flex; align-items: center; gap: 8px; height: 21px; }
  .spec-list svg { width: 12px; height: 12px; }
  .specs-left { left: 193px; }
  .specs-right { left: 323px; }

  .tagline-band {
    position: absolute; left: 0; top: 413px; width: 480px; height: 50px;
    background: var(--teal-bright); color: var(--white);
    font-family: "Signika", sans-serif; font-weight: 700; font-size: 24px;
    display: flex; align-items: center; justify-content: center; padding-left: 20px;
  }

  .info-area { position: absolute; left: 0; top: 463px; width: 480px; height: 170px; display: flex; }
  .info-about { width: 302px; height: 100%; background: linear-gradient(90deg, var(--white), var(--paper)); position: relative; }
  .info-about .footer-brand {
    position: absolute; left: 12px; top: 62px; display: flex; align-items: center; gap: 6px;
    font-family: "Signika", sans-serif; font-weight: 600; font-size: 15px; color: var(--text-grey); letter-spacing: 1px;
  }
  .footer-brand .brand-mark { margin: 0; background: var(--teal-mid); }
  .info-about p {
    position: absolute; left: 133px; top: 28px; width: 162px;
    font-family: "Signika", sans-serif; font-size: 6.6px; line-height: 1.62; color: var(--text-grey);
  }
  .info-contact { flex: 1; background: var(--teal-pale); padding: 53px 0 0 30px; color: var(--teal-deep); font-family: "Signika", sans-serif; font-weight: 600; font-size: 10.5px; line-height: 1.35; }
  .info-contact .web { margin-bottom: 15px; }
  .info-contact .office { margin-bottom: 13px; }
</style>
</head>
<body>
  <article class="flyer">
    <div class="hero-photo" role="img" aria-label="Photo of a two-storey Mediterranean-style home with palm trees, tiled roof and a paved driveway"></div>

    <div class="brand-tab"><span class="brand-mark"></span><span class="brand-name">PelicoHomes</span></div>

    <div class="feature-panel"></div>

    <svg class="sold-badge" viewBox="0 0 116 116" aria-label="Sold at $877,500 – 418 Verbena Hills Drive, Palm Beach Gardens, Florida">
      <defs>
        <path id="arc-top" d="M22 58 A36 36 0 0 1 94 58"/>
        <path id="arc-bottom" d="M17 58 A41 41 0 0 0 99 58"/>
      </defs>
      <polygon fill="var(--badge-red)" points="58,2 64,9 72,4 76,12 85,10 87,19 96,19 95,28 103,31 100,39 107,44 102,51 108,58 102,65 107,72 100,77 103,85 95,88 96,97 87,97 85,106 76,104 72,112 64,107 58,114 52,107 44,112 40,104 31,106 29,97 20,97 21,88 13,85 16,77 9,72 14,65 8,58 14,51 9,44 16,39 13,31 21,28 20,19 29,19 31,10 40,12 44,4 52,9"/>
      <text font-family="Signika, sans-serif" font-weight="600" font-size="8.5" fill="var(--badge-gold)"><textPath href="#arc-top" startOffset="50%" text-anchor="middle">418 Verbena Hills Drive</textPath></text>
      <text font-family="Signika, sans-serif" font-weight="600" font-size="7.5" fill="var(--badge-gold)"><textPath href="#arc-bottom" startOffset="50%" text-anchor="middle">Palm Beach Gardens, Florida</textPath></text>
      <text x="58" y="56" text-anchor="middle" font-family="Signika, sans-serif" font-weight="600" font-size="14" fill="var(--white)">Sold at</text>
      <text x="58" y="76" text-anchor="middle" font-family="Signika, sans-serif" font-weight="700" font-size="21" fill="var(--white)">$877,500</text>
    </svg>

    <div class="recent-sale sale-1">
      <div class="thumb" role="img" aria-label="Photo of a single-storey home with palm tree and lawn"></div>
      <div class="addr">20417 Heron Bluff Circle,<br>West Palm Beach, Florida</div>
      <div class="price">Sold for $380,000</div>
    </div>
    <div class="recent-sale sale-2">
      <div class="thumb" role="img" aria-label="Photo of a grey home with landscaped front garden"></div>
      <div class="addr">4718 Tierra Linda Ct,<br>Boca Raton, FL 33431</div>
      <div class="price">Sold for $415,000</div>
    </div>
    <div class="recent-sale sale-3">
      <div class="thumb" role="img" aria-label="Photo of a ranch-style home with wide lawn"></div>
      <div class="addr">382 Thistle Road,<br>Greenacres, Florida</div>
      <div class="price">Sold for $234,500</div>
    </div>

    <h1 class="headline">ELEGANT<br>HOMES<br>FOR SALE</h1>

    <ul class="spec-list specs-left">
      <li><svg viewBox="0 0 12 12"><path d="M1 6.5 L4.5 10 L11 2" fill="none" stroke="var(--tick-red)" stroke-width="2.4"/></svg>3 Bedrooms</li>
      <li><svg viewBox="0 0 12 12"><path d="M1 6.5 L4.5 10 L11 2" fill="none" stroke="var(--tick-red)" stroke-width="2.4"/></svg>2 Bathrooms</li>
    </ul>
    <ul class="spec-list specs-right">
      <li><svg viewBox="0 0 12 12"><path d="M1 6.5 L4.5 10 L11 2" fill="none" stroke="var(--tick-red)" stroke-width="2.4"/></svg>Built in 2012</li>
      <li><svg viewBox="0 0 12 12"><path d="M1 6.5 L4.5 10 L11 2" fill="none" stroke="var(--tick-red)" stroke-width="2.4"/></svg>2 Car Garages</li>
    </ul>

    <div class="tagline-band">An Elegant Home with Beach Views!</div>

    <section class="info-area">
      <div class="info-about">
        <div class="footer-brand"><span class="brand-mark"></span>PelicoHomes</div>
        <p>Lorem ipsum dolor sit amet, consectetur adipiscing elit. In sodales, nulla sit amet ultricies lobortis, arcu sapien rhoncus eros, eget dictum mi erat vitae arcu. Sed elementum ac enim sit amet semper. Donec est velit, porttitor ut tortor consequat, tempus imperdiet dolor. Sed suscipit, lectus ut imperdiet auctor, leo est vestibulum tellus. Sed elementum ac enim sit amet semper. Donec est velit, porttitor ut tortor consequat, tempus imperdiet dolor.</p>
      </div>
      <div class="info-contact">
        <div class="web">www.pelicohomes-example.com</div>
        <div class="office">561-402-1186<br>Palm Beach County</div>
        <div class="office">954-238-4417<br>Broward County</div>
      </div>
    </section>
  </article>
</body>
</html>
```